Electrical company business card design.

Hi, were an electrical company in Harbourview New Zealand called Quarneth Ltd. We focus mainly on high end residential and commercial so the card would be targeted towards that.
The card will be for myself, i am the director of the company.
Name: Derek Olstow
Position: Director/electrician
Phone: 021 387 9415
Email: derek@quarneth.co.nz
Location: Harbourview
As for colors the the blue color in the logo is preferred, i also don't mind a black background option.
Target Market(s)
High end residential and commercial
Industry/Entity Type
Electrician
Contact Information for Business Card
Name: Derek Olstow Position: Director/Electrician Phone: 021 387 9415, Email: derek@quarneth.co.nz, Location: Harbourview

```html
<!DOCTYPE html>
<html lang="en">
<head>
<meta charset="utf-8">
<title>Quarneth Ltd – Business Card</title>
<link rel="stylesheet" href="https://fonts.googleapis.com/css2?family=Montserrat:wght@400;600;700;800&display=swap">
<style>
  :root {
    --canvas-bg: #2a2c30;
    --card-black: #141414;
    --card-white: #ffffff;
    --brand-blue: #0a57b0;
    --brand-blue-bright: #1f7fe0;
    --steel: #b9bec4;
    --steel-dark: #6f747a;
    --ink: #3a3d42;
    --photo-dark: #3c3c3c;
    --photo-light: #bdbdbd;
  }
  * { box-sizing: border-box; margin: 0; padding: 0; }
  html, body {
    width: 1200px; height: 900px; overflow: hidden;
    background: var(--canvas-bg);
    font-family: "Montserrat", Arial, sans-serif;
  }
  .canvas { position: relative; width: 1200px; height: 900px; }
  .card {
    position: absolute; left: 300px; width: 600px; height: 340px;
    border-radius: 26px; overflow: hidden;
    box-shadow: 0 18px 40px rgba(0,0,0,.45);
  }
  /* Front: black */
  .card-front { top: 70px; background: var(--card-black); }
  .front-brand {
    position: absolute; inset: 0;
    display: flex; flex-direction: column; align-items: center; justify-content: center; gap: 14px;
  }
  .brand-row { display: flex; align-items: center; gap: 16px; }
  .brand-mark {
    width: 34px; height: 34px; border-radius: 50%;
    background: var(--brand-blue-bright);
  }
  .front-brand .brand-name {
    font-size: 62px; font-weight: 700; letter-spacing: 4px; color: var(--steel);
  }
  .front-brand .tagline {
    font-size: 17px; font-weight: 700; letter-spacing: 3px; color: var(--steel-dark);
  }
  /* Back: white */
  .card-back { top: 490px; background: var(--card-white); }
  .back-shapes { position: absolute; inset: 0; }
  .back-brand { position: absolute; top: 34px; right: 40px; text-align: right; }
  .back-brand .brand-row { justify-content: flex-end; gap: 12px; }
  .back-brand .brand-mark { width: 26px; height: 26px; background: var(--brand-blue); }
  .back-brand .brand-name {
    font-size: 46px; font-weight: 700; letter-spacing: 3px; color: var(--ink);
  }
  .back-brand .tagline {
    margin-top: 6px; font-size: 12.5px; font-weight: 700; letter-spacing: 2.4px; color: var(--ink);
  }
  .contact { position: absolute; left: 34px; top: 110px; }
  .contact .person-name { font-size: 26px; font-weight: 800; color: var(--brand-blue); line-height: 1.2; }
  .contact .person-role {
    font-size: 13.5px; font-weight: 400; color: var(--ink);
    padding-bottom: 4px; border-bottom: 1px solid var(--brand-blue);
    display: inline-block; margin-top: 2px;
  }
  .contact-line {
    display: flex; align-items: center; gap: 9px;
    font-size: 13px; line-height: 16px; color: var(--ink); margin-top: 6px;
  }
  .contact-line svg { width: 12px; height: 12px; fill: var(--brand-blue); flex: none; }
  .location {
    position: absolute; left: 34px; top: 222px; height: 44px;
    display: flex; align-items: center; gap: 9px;
    font-size: 15px; color: #fff;
  }
  .location svg { width: 13px; height: 13px; fill: #fff; }
</style>
</head>
<body>
<main class="canvas">

  <section class="card card-front" aria-label="Card front">
    <div class="front-brand">
      <div class="brand-row">
        <span class="brand-mark"></span>
        <span class="brand-name">QUARNETH</span>
      </div>
      <span class="tagline">WIRED FOR EXCELLENCE</span>
    </div>
  </section>

  <section class="card card-back" aria-label="Card back">
    <svg class="back-shapes" viewBox="0 0 600 340" width="600" height="340">
      <defs>
        <linearGradient id="photo-tone" x1="0" y1="0" x2="1" y2="1">
          <stop offset="0" stop-color="#9a9a9a"/>
          <stop offset="0.5" stop-color="#4a4a4a"/>
          <stop offset="1" stop-color="#8a8a8a"/>
        </linearGradient>
      </defs>
      <rect class="contact-band" x="0" y="222" width="330" height="44" fill="var(--brand-blue)"/>
      <path role="img" aria-label="Black and white photo of a digital multimeter"
            d="M250 340 C258 300 280 272 330 266 L430 254 C468 250 472 196 512 186 L600 164 L600 248 C520 298 450 328 385 340 Z"
            fill="url(#photo-tone)"/>
    </svg>

    <div class="back-brand">
      <div class="brand-row">
        <span class="brand-mark"></span>
        <span class="brand-name">QUARNETH</span>
      </div>
      <div class="tagline">WIRED FOR EXCELLENCE</div>
    </div>

    <div class="contact">
      <div class="person-name">Derek Olstow</div>
      <div class="person-role">Director/electrician</div>
      <div class="contact-line">
        <svg viewBox="0 0 24 24"><path d="M6.6 10.8a15.5 15.5 0 0 0 6.6 6.6l2.2-2.2a1 1 0 0 1 1-.25 11.4 11.4 0 0 0 3.6.57 1 1 0 0 1 1 1V20a1 1 0 0 1-1 1A17 17 0 0 1 3 4a1 1 0 0 1 1-1h3.5a1 1 0 0 1 1 1c0 1.25.2 2.45.57 3.6a1 1 0 0 1-.25 1z"/></svg>
        <span>021 387 9415</span>
      </div>
      <div class="contact-line">
        <svg viewBox="0 0 24 24"><path d="M2 5h20v14H2z M2 5l10 8 10-8" fill="none" stroke="var(--brand-blue)" stroke-width="2.4"/></svg>
        <span>derek@quarneth.co.nz</span>
      </div>
    </div>

    <div class="location">
      <svg viewBox="0 0 24 24"><path d="M12 2a7 7 0 0 0-7 7c0 5.2 7 13 7 13s7-7.8 7-13a7 7 0 0 0-7-7zm0 9.5A2.5 2.5 0 1 1 12 6.5a2.5 2.5 0 0 1 0 5z"/></svg>
      <span>Harbourview</span>
    </div>
  </section>

</main>
</body>
</html>
```